New Zealand Marlborough Sauvignon Blanc wine packaging design

We need packaging design for our new wine brand, Dunmore Hale. The wine is a New Zealand Marlborough Sauvignon Blanc. We would like the packaging will portray elegance and style with an understated label. We are looking for a label that portrays the elegance of the French Riviera. The label should be round or pill shaped.
Updates

Industry/Entity Type

Wine

Font styles to use
Serif
Sans Serif

Requirements
Must have
• The words in order of importance: Dunmore Hale, Sauvignon Blanc, Marlborough, New Zealand. It should be fit to the bottle posted in the links
Nice to have
• a pill shape or circular shape
Should not have
• Illustrations of wine bottles, wine glasses, or grapes

```html
<!DOCTYPE html>
<html lang="en">
<head>
<meta charset="utf-8">
<title>Dunmore Hale – Sauvignon Blanc Label</title>
<link href="https://fonts.googleapis.com/css2?family=Gloock&family=Alegreya+Sans+SC:wght@500&display=swap" rel="stylesheet">
<style>
  :root {
    --gold: #d69b1f;
    --ink: #1c150f;
    --paper: #ffffff;
    --rule: #ffffff;
  }
  html, body {
    margin: 0;
    padding: 0;
    width: 1200px;
    height: 1200px;
    overflow: hidden;
    background: var(--paper);
  }
  .canvas {
    position: relative;
    width: 1200px;
    height: 1200px;
    background: var(--paper);
  }
  .label {
    position: absolute;
    left: 196px;
    top: 18px;
    width: 806px;
    height: 1148px;
    box-sizing: border-box;
    border: 22px solid var(--gold);
    border-radius: 403px;
    background: var(--ink);
    overflow: hidden;
  }
  .label__pattern-top {
    position: absolute;
    left: 0;
    top: 0;
    width: 100%;
    height: 410px;
    background: linear-gradient(to bottom,
      rgba(214, 155, 31, 0.55) 0%,
      rgba(214, 155, 31, 0.42) 55%,
      rgba(214, 155, 31, 0) 100%);
  }
  .label__pattern-bottom {
    position: absolute;
    left: 0;
    top: 954px;
    width: 100%;
    height: 200px;
    background: linear-gradient(to bottom,
      rgba(214, 155, 31, 0) 0%,
      rgba(214, 155, 31, 0.45) 35%,
      rgba(214, 155, 31, 0.5) 100%);
  }
  .label__brand {
    position: absolute;
    left: 0;
    top: 480px;
    width: 1200px;
    margin: 0;
    text-align: center;
    font-family: "Gloock", Georgia, serif;
    font-weight: 400;
    font-size: 156px;
    line-height: 138px;
    color: var(--gold);
    letter-spacing: -1px;
  }
  .label__rule {
    position: absolute;
    left: 439px;
    top: 824px;
    width: 329px;
    height: 6px;
    background: var(--rule);
  }
  .label__origin {
    position: absolute;
    left: 0;
    top: 872px;
    width: 1200px;
    margin: 0;
    text-align: center;
    font-family: "Alegreya Sans SC", "Helvetica Neue", Arial, sans-serif;
    font-weight: 500;
    font-size: 33px;
    line-height: 40px;
    letter-spacing: 1px;
    color: var(--gold);
  }
</style>
</head>
<body>
  <div class="canvas">
    <div class="label">
      <div class="label__pattern-top" role="img" aria-label="Flowing gold swirl ornament across the top of the label"></div>
      <div class="label__pattern-bottom" role="img" aria-label="Gold wave ornament along the base of the label"></div>
    </div>
    <h1 class="label__brand">Dunmore<br>Hale</h1>
    <div class="label__rule"></div>
    <p class="label__origin">Sauvignon Blanc,<br>Marlborough, New Zealand</p>
  </div>
</body>
</html>
```